PKD Business Card

Looking for a business card for my restaurant group I own. Four different concepts:

Bramblecrest Alehall
Vellory Alehall
Tamrack's Stone Hearth Kitchen
Cobblestead Patty Works

Card doesn't need to include all the logos.

```html
<!DOCTYPE html>
<html lang="en">
<head>
<meta charset="utf-8">
<title>PKD Business Card</title>
<link href="https://fonts.googleapis.com/css2?family=Lato:wght@400;700;900&display=swap" rel="stylesheet">
<style>
  :root {
    --backdrop: #3b3b3d;
    --card-grey: #6d6e71;
    --card-white: #ffffff;
    --gold: #c9a55c;
    --ink: #58595b;
    --rule: #e1e1e1;
  }
  * { box-sizing: border-box; margin: 0; padding: 0; }
  html, body { width: 1200px; height: 1200px; overflow: hidden; }
  body {
    background: var(--backdrop);
    font-family: "Lato", Arial, sans-serif;
    position: relative;
  }
  .card {
    position: absolute;
    left: 260px;
    width: 680px;
    height: 380px;
    box-shadow: 0 18px 40px rgba(0,0,0,.45);
  }
  .card-back {
    top: 150px;
    background: var(--card-grey);
    border-radius: 90px 0 90px 0;
    display: flex;
    flex-direction: column;
    align-items: center;
    justify-content: center;
    color: #fff;
  }
  .card-back .mark {
    font-weight: 900;
    font-size: 96px;
    letter-spacing: 6px;
    color: var(--gold);
    line-height: 1;
  }
  .concepts {
    margin-top: 44px;
    text-align: center;
    font-weight: 700;
    font-size: 15px;
    letter-spacing: .5px;
    line-height: 1.4;
    text-transform: uppercase;
  }
  .card-front {
    top: 620px;
    background: var(--card-white);
    border-radius: 0 90px 0 90px;
    display: flex;
    align-items: center;
    padding: 0 50px;
  }
  .brand {
    width: 280px;
    display: flex;
    flex-direction: column;
    align-items: center;
    color: var(--gold);
    font-weight: 700;
    text-align: center;
  }
  .brand .mark { font-size: 60px; letter-spacing: 5px; line-height: 1; }
  .brand .name { margin-top: 14px; font-size: 22px; letter-spacing: 4px; text-transform: uppercase; line-height: 1.3; }
  .divider {
    width: 1px;
    height: 200px;
    background: var(--rule);
    margin: 0 36px;
  }
  .details { color: var(--ink); font-size: 18px; line-height: 1.45; }
  .person { color: var(--gold); font-weight: 700; font-size: 25px; letter-spacing: 1px; text-transform: uppercase; }
  .role { font-size: 18px; margin-bottom: 8px; }
  .contact { list-style: none; }
  .contact li { display: flex; align-items: center; gap: 10px; }
  .contact svg { width: 15px; height: 15px; fill: var(--gold); flex: none; }
  .address { margin-top: 10px; }
</style>
</head>
<body>
  <section class="card card-back">
    <div class="mark">PKD</div>
    <p class="concepts">
      Bramblecrest Alehall &nbsp;|&nbsp; Vellory Alehall<br>
      Tamrack's Stone Hearth Kitchen &nbsp;|&nbsp; Cobblestead Patty Works
    </p>
  </section>

  <section class="card card-front">
    <div class="brand">
      <div class="mark">PKD</div>
      <div class="name">Parkdale<br>Dining Group</div>
    </div>
    <div class="divider"></div>
    <div class="details">
      <div class="person">Elias Brandt</div>
      <div class="role">Managing Director</div>
      <ul class="contact">
        <li><svg viewBox="0 0 16 16"><path d="M3 1l3 3-2 2c1 2 4 5 6 6l2-2 3 3-2 2C7 15 1 9 1 3z"/></svg>044-555 018 274</li>
        <li><svg viewBox="0 0 16 16"><path d="M1 3h14v10H1z M1 3l7 6 7-6" stroke="#fff" stroke-width="1.2"/></svg>hello@parkdalekd.com</li>
        <li><svg viewBox="0 0 16 16"><circle cx="8" cy="8" r="7"/></svg>www.parkdalekd.com</li>
      </ul>
      <p class="address">421, Address line here<br>Country Name, 45452</p>
    </div>
  </section>
</body>
</html>
```